metal roofing website

I have several domain names and a website that has been built. I need someone to recreate essentially the same website and change some photos and basic design to create the new sites. I have all of the files and c panel access to the lucky winner. If you can do a good job at a fair price I will have 100's of sites to send to you very soon. I have the site built and have all files just need it recreated on my server. the current site is www.dorvanemetalinc.com I am looking to get this done ASAP!!!

```html
<!DOCTYPE html>
<html lang="en">
<head>
<meta charset="utf-8">
<title>About Us – Dorvane Metal Inc</title>
<link href="https://fonts.googleapis.com/css2?family=Roboto+Condensed:wght@700&family=Roboto:wght@400;500&display=swap" rel="stylesheet">
<style>
:root{
  --brand-red:#b52e25;
  --sand:#e7d4c3;
  --ink:#1d1a18;
  --white:#ffffff;
}
*{margin:0;padding:0;box-sizing:border-box}
html,body{width:1147px;height:1200px;overflow:hidden}
body{position:relative;background:var(--white);font-family:"Roboto",sans-serif;color:var(--ink)}
.topbar{position:absolute;left:0;top:0;width:1147px;height:40px;background:var(--brand-red);color:var(--white)}
.topbar__call{position:absolute;right:226px;top:11px;font-family:"Roboto Condensed",sans-serif;font-weight:700;font-size:15px;display:flex;align-items:center;gap:5px;white-space:nowrap}
.social{position:absolute;display:flex;gap:12px}
.social span{width:13px;height:13px;border-radius:50%;background:var(--white);display:block}
.topbar .social{right:116px;top:13px}
.header{position:absolute;left:0;top:40px;width:1147px;height:106px;background:var(--sand)}
.brand{position:absolute;left:104px;top:40px;display:flex;align-items:center;gap:8px;font-family:"Roboto Condensed",sans-serif;font-weight:700;font-size:22px;color:var(--brand-red);text-transform:uppercase}
.brand__mark{width:18px;height:18px;background:var(--brand-red)}
.nav{position:absolute;left:491px;top:53px;display:flex;gap:22px;font-size:12px;letter-spacing:1px}
.nav a{color:var(--ink);text-decoration:none}
.nav a.is-active{color:var(--brand-red)}
.nav-cta{position:absolute;left:904px;top:42px;width:127px;height:35px;border-radius:18px;background:var(--brand-red);color:var(--white);font-size:12px;letter-spacing:1px;display:flex;align-items:center;justify-content:center}
.hero{position:absolute;left:0;top:146px;width:1147px;height:276px;background:linear-gradient(90deg,#3f5a2a 0%,#5d7440 22%,#b4ad94 45%,#bdb8a3 70%,#d1d3d3 100%)}
.about{position:absolute;left:102px;top:492px;width:470px}
.about h1{font-family:"Roboto Condensed",sans-serif;font-weight:700;font-size:27px;color:var(--brand-red);letter-spacing:.5px;line-height:1.1}
.about h2{font-family:"Roboto Condensed",sans-serif;font-weight:700;font-size:19px;color:var(--brand-red);letter-spacing:.5px;line-height:1.1}
.about .h-company{margin-top:42px}
.about .h-what{margin-top:14px}
.about .tagline{margin-top:20px;font-size:13px;font-weight:500}
.about .h-history{margin-top:22px}
.about .history{margin-top:20px;font-size:13px;font-weight:500}
.about-photo{position:absolute;left:592px;top:492px;width:439px;height:293px;background:linear-gradient(180deg,#e9ebe9 0%,#dfe1df 45%,#9aa89a 58%,#5d9a3a 72%,#4f8c2f 100%)}
.footer{position:absolute;left:0;top:855px;width:1147px;height:294px;background:var(--sand);font-size:13px;font-weight:500}
.footer h3{font-family:"Roboto Condensed",sans-serif;font-weight:700;font-size:17px;color:var(--brand-red);letter-spacing:.8px;margin-bottom:13px}
.footer__col{position:absolute;top:59px}
.col-contact{left:102px}
.col-sitemap{left:429px}
.col-hours{left:755px}
.footer p{line-height:25px}
.col-contact .gap{margin-top:12px}
.sitemap{list-style:none}
.sitemap li{line-height:31px;position:relative;padding-left:12px}
.sitemap li::before{content:"";position:absolute;left:0;top:12px;width:4px;height:4px;border-radius:50%;background:var(--brand-red)}
.bottombar{position:absolute;left:0;top:1149px;width:1147px;height:51px;background:var(--brand-red);color:var(--white)}
.bottombar__copy{position:absolute;left:102px;top:17px;font-size:13px;font-weight:500}
.bottombar .social{right:116px;top:19px;gap:17px}
</style>
</head>
<body>
<div class="topbar">
  <div class="topbar__call">
    <svg width="9" height="15" viewBox="0 0 9 15"><rect x="0.8" y="0.8" width="7.4" height="13.4" rx="1.5" fill="none" stroke="#fff" stroke-width="1.6"/><circle cx="4.5" cy="12" r="0.9" fill="#fff"/></svg>
    Call US: 715-555-0194
  </div>
  <div class="social"><span></span><span></span><span></span></div>
</div>

<header class="header">
  <div class="brand"><span class="brand__mark"></span>Dorvane Metal Inc</div>
  <nav class="nav">
    <a href="#">HOME</a>
    <a href="#" class="is-active">ABOUT US</a>
    <a href="#">SERVICES</a>
    <a href="#">GALLERY</a>
    <a href="#">CONTACT US</a>
  </nav>
  <div class="nav-cta">VISUALIZER</div>
</header>

<div class="hero" role="img" aria-label="Photo of a large metal-sided pole building with dormers and a cupola, framed by trees"></div>

<section class="about">
  <h1>ABOUT US</h1>
  <h2 class="h-company">ABOUT OUR COMPANY</h2>
  <h2 class="h-what">WHAT WE DO</h2>
  <p class="tagline">MANUFACTURERS OF QUALITY BUILDING COMPONENTS</p>
  <h2 class="h-history">COMPANY HISTORY</h2>
  <p class="history">We have been proudly serving West central Wisconsin for the past 19 years.</p>
</section>
<div class="about-photo" role="img" aria-label="Photo of a two-storey farmhouse with a metal roof on a green lawn beside a gravel drive"></div>

<footer class="footer">
  <div class="footer__col col-contact">
    <h3>DORVANE METAL INC</h3>
    <p>Phone:</p>
    <p>715-555-0165</p>
    <p class="gap">Fax:</p>
    <p>715-555-0194</p>
  </div>
  <div class="footer__col col-sitemap">
    <h3>SITEMAP</h3>
    <ul class="sitemap">
      <li>Home</li><li>About Us</li><li>Services</li><li>Gallery</li><li>Contact Us</li>
    </ul>
  </div>
  <div class="footer__col col-hours">
    <h3>HOURS</h3>
    <p>Monday – Friday: 7am – 5pm</p>
    <p>Saturday: 7am – 12pm</p>
    <p>Sunday: Closed</p>
  </div>
</footer>

<div class="bottombar">
  <div class="bottombar__copy">Copyright © 2018 Dorvane Metal Inc. All rights reserved.</div>
  <div class="social"><span></span><span></span><span></span></div>
</div>
</body>
</html>
```